依頼詳細
以前こちらで作成して頂いた雰囲気の内容でお願いします。
※添付チラシ

記載項目
・もえぎうたのロゴマークを入れてください。
https://moegiuta.or.jp/event-t/2020-03-14-2 このアドレス用のQRコードを記載してください。
・添付しました画像を使用してください。
サイズ
A4
ページ数
片面
希望イメージ
シンプル 複雑
単色 カラフル
暗い 明るい
日常 高級
遊び心 厳粛
未来的 伝統的
女性的 男性的
希望する色
納品ファイル
補足説明
■ 選んだ理由

ご提案いただきありがとうございました。
どれも良いご提案で悩みましたが、色合いや、雰囲気、読みやすさ、
これから家づくりを考える対象年齢層などを考慮して
選択させて頂きました。

■ 提案者全員のお礼・コメント

多くのご提案を頂きありがとうございました。<m(__)m>

```html
<!DOCTYPE html>
<html lang="ja">
<head>
<meta charset="utf-8">
<title>「家づくり」はじめの一歩 | 暮らしの「学び場」セミナー</title>
<link href="https://fonts.googleapis.com/css2?family=Noto+Sans+JP:wght@400;500;700;900&family=Noto+Serif+JP:wght@700;900&family=M+PLUS+Rounded+1c:wght@700;800&display=swap" rel="stylesheet">
<style>
  :root{
    --pink:#e9748a;
    --coral:#ee7c63;
    --coral-deep:#e2604f;
    --ink:#4b3a35;
    --ink-soft:#6d5c56;
    --yellow:#f6d44c;
    --blush:#fdeeee;
    --blush-strong:#f9d9dc;
    --white:#ffffff;
    --line:#efc2c8;
  }
  *{box-sizing:border-box;margin:0;padding:0}
  html,body{width:857px;height:1200px;overflow:hidden;background:var(--white)}
  body{font-family:"Noto Sans JP",sans-serif;color:var(--ink)}
  .flyer{position:relative;width:857px;height:1200px;overflow:hidden;background:var(--white)}
  .top-wash{position:absolute;left:0;top:0;width:857px;height:90px;background:linear-gradient(180deg,var(--blush-strong),var(--white))}
  .bunting{position:absolute;left:0;top:0;width:857px;height:70px;background:linear-gradient(90deg,rgba(246,212,76,.35),rgba(233,116,138,.3),rgba(238,124,99,.3));opacity:.7}
  .series-label{position:absolute;left:205px;top:32px;width:345px;height:34px;border:2px solid var(--pink);background:var(--white);
    display:flex;align-items:center;justify-content:center;font-weight:700;font-size:19px;color:var(--pink);letter-spacing:.06em}
  .title{position:absolute;left:384px;top:96px;width:90px;height:600px;writing-mode:vertical-rl;white-space:nowrap;
    font-family:"Noto Serif JP",serif;font-weight:900;color:var(--ink);line-height:90px}
  .title .main{font-size:62px}
  .title .sub{font-size:34px;padding-block-start:14px;display:inline-block}
  .lead{position:absolute;writing-mode:vertical-rl;font-size:14.5px;line-height:1.95;font-weight:500;color:var(--ink)}
  .lead-right{left:548px;top:86px;height:186px;width:270px}
  .lead-left{left:132px;top:98px;height:190px;width:236px}
  .lead em{font-style:normal;color:var(--pink);font-weight:700}
  .before{position:absolute;left:38px;top:300px;width:330px}
  .before h2{font-size:18px;font-weight:700;color:var(--ink);padding-bottom:4px;border-bottom:2px solid var(--pink);display:flex;gap:8px;align-items:center}
  .before h2::before{content:"";width:10px;height:10px;background:var(--pink);border-radius:50%}
  .before ul{list-style:none;margin-top:10px}
  .before li{font-size:14px;font-weight:700;color:var(--pink);line-height:1.9}
  .before li::before{content:"● ";font-size:11px}
  .before p{margin-top:8px;font-size:11px;line-height:1.7;color:var(--ink-soft)}
  .photo{position:absolute;left:28px;top:486px;width:350px;height:498px;border-radius:6px;
    background:linear-gradient(160deg,#f5ede4 0%,#e8d9c8 55%,#d9c2aa 100%)}
  .bubble{position:absolute;left:236px;top:560px;width:130px;height:130px;border-radius:50%;background:var(--yellow);
    display:flex;align-items:center;justify-content:center;text-align:center;font-family:"M PLUS Rounded 1c",sans-serif;font-weight:800;font-size:16px;line-height:1.4;color:var(--ink)}
  .free-band{position:absolute;left:512px;top:328px;width:318px;height:24px;background:var(--pink);color:var(--white);
    font-size:13px;font-weight:700;display:flex;align-items:center;justify-content:center;letter-spacing:.04em}
  .info{position:absolute;left:512px;top:360px;width:318px}
  .info .row{display:flex;align-items:center;gap:12px;margin-bottom:6px}
  .info .tag{flex:none;width:58px;height:24px;border:1.5px solid var(--pink);color:var(--pink);font-size:13px;font-weight:700;display:flex;align-items:center;justify-content:center}
  .info .date{font-size:36px;font-weight:900;color:var(--pink);line-height:1}
  .info .date small{font-size:20px}
  .info .time{font-size:32px;font-weight:900;color:var(--pink);line-height:1}
  .info .detail{font-size:12px;line-height:1.6;color:var(--ink)}
  .info .detail dt{display:inline;font-weight:700}
  .info .detail dd{display:inline;margin-right:2px}
  .org{position:absolute;left:512px;top:598px;width:215px}
  .org .caption{font-size:11px;color:var(--ink-soft)}
  .org .name{display:flex;align-items:center;gap:8px;margin-top:6px;font-family:"M PLUS Rounded 1c",sans-serif;font-weight:800;font-size:30px;color:var(--coral-deep);white-space:nowrap}
  .org .name::before{content:"";width:26px;height:26px;border-radius:50%;background:var(--coral-deep)}
  .qr{position:absolute;left:744px;top:592px;width:84px;height:84px;background:var(--white);border:6px solid var(--ink)}
  .qr::after{content:"";position:absolute;inset:14px;background:var(--ink-soft);opacity:.35}
  .phone{position:absolute;left:512px;top:684px;width:318px;display:flex;align-items:center;gap:8px;color:var(--coral-deep);font-weight:900;font-size:27px;line-height:1;white-space:nowrap}
  .phone .hours{font-size:10.5px;color:var(--ink-soft);font-weight:500;line-height:1.3}
  .note{position:absolute;left:512px;top:732px;width:318px;font-size:11.5px;line-height:1.75;color:var(--ink-soft)}
  .cta-band{position:absolute;left:0;top:992px;width:857px;height:60px;background:linear-gradient(90deg,var(--coral),var(--pink));
    display:flex;align-items:center;justify-content:center;gap:14px;color:var(--white);font-weight:900}
  .cta-band .text{font-size:22px;letter-spacing:.03em}
  .cta-band .mins{font-size:44px;line-height:1}
  .cta-band .mins small{font-size:22px}
  .agenda{position:absolute;left:0;top:1052px;width:857px;height:148px;background:var(--blush);padding:12px 30px 0}
  .agenda h3{display:inline-block;background:var(--pink);color:var(--white);font-size:13px;font-weight:700;padding:3px 14px;border-radius:12px}
  .agenda ul{list-style:none;display:grid;grid-template-columns:repeat(3,1fr);gap:6px 16px;margin-top:10px;background:var(--white);border:1.5px solid var(--line);border-radius:6px;padding:12px 16px}
  .agenda li{display:flex;align-items:center;gap:6px;font-size:13px;font-weight:500;color:var(--ink)}
  .agenda li svg{flex:none}
</style>
</head>
<body>
<main class="flyer">
  <div class="top-wash"></div>
  <div class="bunting" role="img" aria-label="パステルカラーの三角旗のガーランド"></div>

  <div class="series-label">暮らしの「学び場」セミナー</div>

  <h1 class="title"><span class="main">「家づくり」</span><span class="sub">はじめの一歩</span></h1>

  <p class="lead lead-right">家を建てることは人生の大きな決断です。大切な家族が安心して暮らせる住まいを考えるために、まずは正しい知識を身につけましょう。専門家がわかりやすくお伝えします。</p>

  <p class="lead lead-left">満足のいく家づくりのために、<em>知っておきたいこと</em>があります。建てた後に後悔しないよう、<em>家族で話し合うきっかけ</em>にしてください。</p>

  <section class="before">
    <h2>家を建てる前に</h2>
    <ul>
      <li>夫婦（家族）で決めておくべきことがある</li>
      <li>計画を進める順番がある</li>
      <li>判断基準を持っておく必要がある</li>
    </ul>
    <p>それぞれについて、実際の事例を交えながら、これからの暮らしに役立つ考え方をご紹介します。</p>
  </section>

  <div class="photo" role="img" aria-label="手のひらにのせた家の模型の写真"></div>
  <div class="bubble">家族の<br>一生に<br>かかわること</div>

  <div class="free-band">参加・保護者無料、お子様連れOK</div>
  <section class="info">
    <div class="row"><span class="tag">開催日</span><span class="date">3月14日<small>(土)</small></span></div>
    <div class="row"><span class="tag">時　間</span><span class="time">13:30～15:00</span></div>
    <dl class="detail">
      <dt>会場：</dt><dd>くらしの灯り会館 2F 研修室（みどり市さくら町1-2-3）</dd><br>
      <dt>講師：</dt><dd>もえぎうた 住まいアドバイザー</dd><br>
      <dt>定員：</dt><dd>10組（先着順）</dd><br>
      <dt>申込方法：</dt><dd>電話またはWebからお申込みください</dd>
    </dl>
  </section>

  <div class="org">
    <div class="caption">一般社団法人 くらしの灯り協会</div>
    <div class="name">もえぎうた</div>
  </div>
  <div class="qr" role="img" aria-label="申込ページ moegiuta.or.jp/event-t/2020-03-14-2 へのQRコード"></div>

  <div class="phone">
    <svg width="24" height="24" viewBox="0 0 24 24" aria-hidden="true"><path fill="currentColor" d="M6.6 10.8a15.1 15.1 0 0 0 6.6 6.6l2.2-2.2a1 1 0 0 1 1-.25 11.4 11.4 0 0 0 3.6.57 1 1 0 0 1 1 1V20a1 1 0 0 1-1 1A17 17 0 0 1 3 4a1 1 0 0 1 1-1h3.5a1 1 0 0 1 1 1c0 1.25.2 2.45.57 3.57a1 1 0 0 1-.25 1z"/></svg>
    0120-555-018
    <span class="hours">受付<br>9:00～17:00</span>
  </div>

  <p class="note">セミナーでは、家づくりを始める前に押さえておきたい基本をやさしく解説します。資金計画や土地選び、住まい方の考え方など、ご家族の将来を見据えた判断に役立つ内容です。お気軽にご参加ください。詳細はWebページ（moegiuta.or.jp/event-t/2020-03-14-2）でもご覧いただけます。</p>

  <div class="cta-band">
    <span class="text">だから、家づくりを始める前に知っておくべきこと</span>
    <span class="mins">90<small>分</small></span>
  </div>

  <section class="agenda">
    <h3>当日お話させていただく内容</h3>
    <ul>
      <li><svg width="16" height="16" viewBox="0 0 16 16"><rect x="1" y="1" width="14" height="14" fill="none" stroke="#e9748a" stroke-width="1.5"/><path d="M4 8l3 3 5-6" fill="none" stroke="#e9748a" stroke-width="2"/></svg>家づくりの流れと順番</li>
      <li><svg width="16" height="16" viewBox="0 0 16 16"><rect x="1" y="1" width="14" height="14" fill="none" stroke="#e9748a" stroke-width="1.5"/><path d="M4 8l3 3 5-6" fill="none" stroke="#e9748a" stroke-width="2"/></svg>無理のない資金計画</li>
      <li><svg width="16" height="16" viewBox="0 0 16 16"><rect x="1" y="1" width="14" height="14" fill="none" stroke="#e9748a" stroke-width="1.5"/><path d="M4 8l3 3 5-6" fill="none" stroke="#e9748a" stroke-width="2"/></svg>土地選びのポイント</li>
      <li><svg width="16" height="16" viewBox="0 0 16 16"><rect x="1" y="1" width="14" height="14" fill="none" stroke="#e9748a" stroke-width="1.5"/><path d="M4 8l3 3 5-6" fill="none" stroke="#e9748a" stroke-width="2"/></svg>家族で決めておくこと</li>
      <li><svg width="16" height="16" viewBox="0 0 16 16"><rect x="1" y="1" width="14" height="14" fill="none" stroke="#e9748a" stroke-width="1.5"/><path d="M4 8l3 3 5-6" fill="none" stroke="#e9748a" stroke-width="2"/></svg>住宅会社の選び方</li>
      <li><svg width="16" height="16" viewBox="0 0 16 16"><rect x="1" y="1" width="14" height="14" fill="none" stroke="#e9748a" stroke-width="1.5"/><path d="M4 8l3 3 5-6" fill="none" stroke="#e9748a" stroke-width="2"/></svg>よくある失敗例</li>
    </ul>
  </section>
</main>
</body>
</html>
```